Flyer-Design für Business Center
Zielgruppe
Wir sind Co-Working /Business Center Anbieter auf Basis eines Mitgliedschaft Konzeptes. Bei uns kann man Arbeitsplätze und Büroräume mit Kaffee und Wasser in einer Lounge anmieten. Dazu bieten wir Bedarfsgerechte Mitgliedschaften an. Unsere Kunden sind Kreative, Programmierer, Freiberufler aber auch größere Unternehmen.
Aufgabenstellung
DIN LANG A 4, der Flyer wird gedruckt und kommt in Aussteller. Er soll als Eye Catcher den Preis ab 69,90 für 4 Wochen beinhalten. In diesem Preis ist alles inclusive. Also Wasser, Kaffee, Cappuccino, Drucker, Kopierer, Möbel, Putzfrau, Schreibtisch. Bürostuhl. Gleichzeitig soll der Flyer auch als PDF versendet werden können.
Weitere Information findet man auf unserer Webseite www.kranichfeldwerk.com

```html
<!DOCTYPE html>
<html lang="de">
<head>
<meta charset="utf-8">
<title>Kranichfeld Werk – Flyer DIN lang</title>
<link href="https://fonts.googleapis.com/css2?family=Quicksand:wght@400;500;700&display=swap" rel="stylesheet">
<style>
:root{
  --blue:#0b9bd7;
  --blue-dark:#0a86bb;
  --yellow:#f7e51c;
  --grey-text:#8e959b;
  --grey-light:#eef2f5;
  --grey-bar:#b9bec2;
  --paper:#fafbfc;
  --white:#ffffff;
}
*{box-sizing:border-box;margin:0;padding:0}
html,body{width:1200px;height:1200px;overflow:hidden;background:var(--white);font-family:'Quicksand',sans-serif}
.canvas{position:relative;width:1200px;height:1200px}
.page{position:absolute;background:linear-gradient(180deg,var(--paper),#f1f4f7);box-shadow:0 2px 8px rgba(0,0,0,.12);overflow:hidden}
.page--front{left:96px;top:155px;width:472px;height:940px}
.page--back{left:671px;top:153px;width:481px;height:947px}
.abs{position:absolute}
.top-band{left:0;top:0;width:100%;height:8px;background:var(--blue)}
.photo{position:absolute}
.photo--lounge{left:0;top:8px;width:472px;height:288px;background:linear-gradient(160deg,#d9e4ea 0%,#f4f6f7 40%,#b9c3c9 75%,#8d979c 100%)}
.photo--hall{left:210px;top:307px;width:256px;height:153px;background:linear-gradient(180deg,#e9ebeb 0%,#cfd2d1 55%,#b4b8b8 100%)}
.photo--cabinets{left:0;top:8px;width:481px;height:174px;background:linear-gradient(180deg,#9bb07f 0%,#e7e9e8 35%,#d8dbdb 75%,#3b3f42 100%)}
.photo--building{left:0;top:447px;width:237px;height:148px;background:linear-gradient(180deg,#dfe6ea 0%,#c6ccd0 55%,#6e7f63 100%)}
.photo--map{left:0;top:679px;width:237px;height:180px;background:linear-gradient(135deg,#cfe3ee 0%,#eceeef 30%,#e4e6e7 70%,#d6e8d0 100%)}
.brand{left:14px;top:50px;display:flex;align-items:center;gap:8px;color:var(--blue);font-weight:500;font-size:21px;line-height:1}
.brand__dot{width:14px;height:14px;border-radius:50%;background:var(--blue)}
.price{left:15px;top:235px;width:182px;height:153px;background:var(--blue);text-align:center}
.price__lead{margin-top:10px;color:var(--yellow);font-size:16px}
.price__rule{width:160px;height:2px;background:var(--white);margin:9px auto 0}
.price__amount{margin-top:6px;color:var(--yellow);font-weight:700;font-size:40px;line-height:52px}
.price__note{margin-top:8px;color:var(--white);font-size:16px}
.fineprint{left:14px;top:401px;width:180px;color:var(--grey-text);font-size:8.5px;line-height:11px}
.rule-blue{background:var(--blue)}
.heading{color:var(--grey-text);font-size:23px;font-weight:400;white-space:nowrap;padding-left:12px;border-left:3px solid var(--blue);line-height:20px}
.heading span{color:var(--blue)}
.heading__line{height:1.5px;background:var(--blue)}
.service{position:absolute;width:130px;text-align:center;color:var(--grey-text);font-size:16px}
.service svg{display:block;margin:0 auto 12px}
.divider{width:1px;background:#dde3e7}
.footer-site{background:var(--blue);color:var(--white);font-size:15px;display:flex;align-items:center;justify-content:center}
.footer-company{color:var(--grey-text);font-size:8.5px;line-height:11px}
.footer-contact{color:var(--blue);font-size:8.5px;line-height:17px}
.footer-contact svg{vertical-align:-2px;margin-right:4px}
.footer-bar{background:var(--grey-bar)}
.address{color:var(--blue);font-weight:700;font-size:10px;line-height:14px;text-align:center;width:110px}
.benefits{color:var(--grey-text);font-size:10.5px;line-height:14.5px;list-style:none}
.benefits__title{color:var(--blue);font-weight:700;font-size:10.5px;margin-bottom:15px}
.benefits li svg{vertical-align:-1px;margin-right:5px}
.body-copy{color:var(--grey-text);font-size:10.5px;line-height:14.4px;width:205px}
</style>
</head>
<body>
<div class="canvas">

  <!-- Front page -->
  <section class="page page--front">
    <div class="abs top-band"></div>
    <div class="photo photo--lounge" role="img" aria-label="Helle Lounge mit weißen Sesseln, Tischen und Pflanzen vor großen Fenstern"></div>
    <div class="abs brand"><span class="brand__dot"></span>Kranichfeld Werk</div>
    <div class="abs price">
      <p class="price__lead">Büroräume ab</p>
      <div class="price__rule"></div>
      <p class="price__amount">69,90€</p>
      <div class="price__rule"></div>
      <p class="price__note">für 4 Wochen</p>
    </div>
    <div class="photo photo--hall" role="img" aria-label="Großzügiger Büroraum mit hohen Bogenfenstern und Backsteinwänden"></div>
    <p class="abs fineprint">Inklusive Mehrwertsteuer. Preise gelten pro Arbeitsplatz. Alle Leistungen sind im Monatspreis enthalten, ohne weitere Nebenkosten.</p>
    <div class="abs rule-blue" style="left:11px;top:470px;width:461px;height:7px"></div>

    <h2 class="abs heading" style="left:122px;top:503px">Leistungen <span>Inklusive</span></h2>
    <div class="abs heading__line" style="left:136px;top:530px;width:210px"></div>

    <div class="abs divider" style="left:157px;top:560px;height:300px"></div>
    <div class="abs divider" style="left:318px;top:560px;height:300px"></div>

    <div class="service" style="left:12px;top:562px">
      <svg width="58" height="58" viewBox="0 0 58 58"><circle cx="29" cy="29" r="27" fill="#fff" stroke="#0b9bd7" stroke-width="2"/><rect x="17" y="20" width="14" height="18" fill="#0b9bd7"/><path d="M31 22h11M37 22v16M33 38h8" stroke="#0b9bd7" stroke-width="2.4" fill="none"/></svg>Möbel</div>
    <div class="service" style="left:172px;top:562px">
      <svg width="58" height="58" viewBox="0 0 58 58"><circle cx="29" cy="29" r="27" fill="#fff" stroke="#0b9bd7" stroke-width="2"/><path d="M15 26a20 20 0 0 1 28 0M19 30a14 14 0 0 1 20 0M23 34a8 8 0 0 1 12 0" stroke="#0b9bd7" stroke-width="3" fill="none" stroke-linecap="round"/><circle cx="29" cy="39" r="2.5" fill="#0b9bd7"/></svg>WiFi</div>
    <div class="service" style="left:330px;top:562px">
      <svg width="58" height="58" viewBox="0 0 58 58"><circle cx="29" cy="29" r="27" fill="#fff" stroke="#0b9bd7" stroke-width="2"/><rect x="23" y="14" width="12" height="15" rx="3" fill="#0b9bd7"/><path d="M19 31h20M29 31v8M20 42l9-3 9 3M18 25v6M40 25v6" stroke="#0b9bd7" stroke-width="2.4" fill="none"/></svg>Bürostuhl</div>

    <div class="service" style="left:12px;top:667px">
      <svg width="58" height="58" viewBox="0 0 58 58"><circle cx="29" cy="29" r="27" fill="#fff" stroke="#0b9bd7" stroke-width="2"/><rect x="21" y="15" width="16" height="8" fill="none" stroke="#0b9bd7" stroke-width="2.2"/><rect x="16" y="23" width="26" height="12" rx="2" fill="#0b9bd7"/><rect x="21" y="31" width="16" height="12" fill="#fff" stroke="#0b9bd7" stroke-width="2.2"/></svg>Drucker</div>
    <div class="service" style="left:172px;top:667px">
      <svg width="58" height="58" viewBox="0 0 58 58"><circle cx="29" cy="29" r="27" fill="#fff" stroke="#0b9bd7" stroke-width="2"/><rect x="25" y="15" width="14" height="18" fill="#0b9bd7"/><rect x="19" y="23" width="14" height="18" fill="#0b9bd7" stroke="#fff" stroke-width="1.5"/></svg>Kopierer</div>
    <div class="service" style="left:330px;top:667px">
      <svg width="58" height="58" viewBox="0 0 58 58"><circle cx="29" cy="29" r="27" fill="#fff" stroke="#0b9bd7" stroke-width="2"/><path d="M40 15L30 30" stroke="#0b9bd7" stroke-width="2.4"/><path d="M24 29l9 6-6 9-10-6z" fill="#0b9bd7"/><path d="M20 17v5M17.5 19.5h5M36 34v4M34 36h4" stroke="#0b9bd7" stroke-width="1.6"/></svg>Reinigung</div>

    <div class="service" style="left:12px;top:773px">
      <svg width="58" height="58" viewBox="0 0 58 58"><circle cx="29" cy="29" r="27" fill="#fff" stroke="#0b9bd7" stroke-width="2"/><path d="M20 15h18l-3 28H23z" fill="none" stroke="#0b9bd7" stroke-width="2.2"/><path d="M21.5 25h15l-2 16h-11z" fill="#0b9bd7"/></svg>Wasser</div>
    <div class="service" style="left:172px;top:773px">
      <svg width="58" height="58" viewBox="0 0 58 58"><circle cx="29" cy="29" r="27" fill="#fff" stroke="#0b9bd7" stroke-width="2"/><path d="M18 26h18v8a9 9 0 0 1-18 0z" fill="#0b9bd7"/><path d="M36 28a4 4 0 0 1 0 8" stroke="#0b9bd7" stroke-width="2.4" fill="none"/><path d="M24 15c-2 3 2 5 0 8M30 15c-2 3 2 5 0 8" stroke="#0b9bd7" stroke-width="1.8" fill="none"/></svg>Kaffee</div>
    <div class="service" style="left:330px;top:773px">
      <svg width="58" height="58" viewBox="0 0 58 58"><circle cx="29" cy="29" r="27" fill="#fff" stroke="#0b9bd7" stroke-width="2"/><path d="M18 26h20v4a10 10 0 0 1-20 0z" fill="#0b9bd7"/><path d="M38 27a4 4 0 0 1 0 8" stroke="#0b9bd7" stroke-width="2.2" fill="none"/><path d="M14 41h30" stroke="#0b9bd7" stroke-width="2.4" stroke-linecap="round"/><path d="M25 15c-2 3 2 5 0 8M31 15c-2 3 2 5 0 8" stroke="#0b9bd7" stroke-width="1.8" fill="none"/></svg>Cappuccino</div>

    <div class="abs footer-bar" style="left:184px;top:932px;width:288px;height:8px"></div>
    <div class="abs footer-site" style="left:15px;top:890px;width:162px;height:50px">kranichfeldwerk.com</div>
    <p class="abs footer-company" style="left:195px;top:886px">Kranichfeld Werk GmbH<br>Ahornweg 24<br>53117 Bonn</p>
    <p class="abs footer-contact" style="left:327px;top:884px">
      <svg width="10" height="10" viewBox="0 0 10 10"><path d="M2 1l2 2-1 1.5a6 6 0 0 0 2.5 2.5L7 6l2 2-1.5 1.5C4 9 1 6 .5 2.5z" fill="none" stroke="#0b9bd7" stroke-width=".9"/></svg>+49-228-555010-00<br>
      <svg width="10" height="8" viewBox="0 0 10 8"><rect x=".5" y=".5" width="9" height="7" fill="none" stroke="#0b9bd7"/><path d="M.5.5l4.5 4 4.5-4" fill="none" stroke="#0b9bd7"/></svg>info@kranichfeldwerk.com</p>
  </section>

  <!-- Back page -->
  <section class="page page--back">
    <div class="abs top-band"></div>
    <div class="photo photo--cabinets" role="img" aria-label="Weiße Büroschränke mit Pflanzkübeln vor einer Fensterfront"></div>
    <div class="abs rule-blue" style="left:16px;top:182px;width:465px;height:7px"></div>

    <h2 class="abs heading" style="left:137px;top:214px">Büro <span>Mohnheim</span></h2>
    <div class="abs heading__line" style="left:152px;top:241px;width:178px"></div>

    <svg class="abs" style="left:41px;top:261px" width="60" height="60" viewBox="0 0 60 60"><circle cx="30" cy="30" r="28" fill="#fff" stroke="#0b9bd7" stroke-width="2"/><path d="M30 46c-8-9-12-15-12-20a12 12 0 0 1 24 0c0 5-4 11-12 20z" fill="#0b9bd7"/><circle cx="30" cy="26" r="6" fill="#fff"/></svg>
    <p class="abs address" style="left:15px;top:325px">Birkenstraße 8,<br>40789 Monheim<br>am Rhein</p>
    <div class="abs divider" style="left:155px;top:277px;height:90px"></div>
    <ul class="abs benefits" style="left:196px;top:266px">
      <li class="benefits__title"><svg width="8" height="8" viewBox="0 0 8 8"><circle cx="4" cy="4" r="3" fill="none" stroke="#0b9bd7" stroke-width="1.6"/></svg>Vorteile des Standortes:</li>
      <li><svg width="8" height="8" viewBox="0 0 8 8"><circle cx="4" cy="4" r="3.5" fill="none" stroke="#8e959b" stroke-width=".8"/><path d="M2.3 4l1.2 1.2L5.8 2.8" fill="none" stroke="#8e959b" stroke-width=".9"/></svg>Günstigste Gewerbesteuer in NRW</li>
      <li><svg width="8" height="8" viewBox="0 0 8 8"><circle cx="4" cy="4" r="3.5" fill="none" stroke="#8e959b" stroke-width=".8"/><path d="M2.3 4l1.2 1.2L5.8 2.8" fill="none" stroke="#8e959b" stroke-width=".9"/></svg>Zentrale Lage in der Stadt</li>
      <li><svg width="8" height="8" viewBox="0 0 8 8"><circle cx="4" cy="4" r="3.5" fill="none" stroke="#8e959b" stroke-width=".8"/><path d="M2.3 4l1.2 1.2L5.8 2.8" fill="none" stroke="#8e959b" stroke-width=".9"/></svg>Gute Anbindung an Autobahn</li>
      <li><svg width="8" height="8" viewBox="0 0 8 8"><circle cx="4" cy="4" r="3.5" fill="none" stroke="#8e959b" stroke-width=".8"/><path d="M2.3 4l1.2 1.2L5.8 2.8" fill="none" stroke="#8e959b" stroke-width=".9"/></svg>Parkplätze vorhanden</li>
    </ul>

    <h2 class="abs heading" style="left:137px;top:390px">Über das <span>Büro</span></h2>
    <div class="abs heading__line" style="left:155px;top:418px;width:172px"></div>

    <div class="photo photo--building" role="img" aria-label="Mehrstöckiges weißes Bürogebäude mit Bäumen"></div>
    <p class="abs body-copy" style="left:259px;top:445px">Unsere Niederlassung in Monheim am Rhein überzeugt durch ein breites Spektrum an Angeboten. Neben einer idealen Verkehrsanbindung und modernen Büros erwartet dich hier der günstigste Gewerbesteuersatz von ganz Nordrhein-Westfalen. Du sparst bares Geld und profitierst von einer zentralen und behaglichen Lage.</p>
    <div class="abs rule-blue" style="left:261px;top:592px;width:220px;height:5px"></div>

    <h2 class="abs heading" style="left:137px;top:623px">Lage des <span>Büros</span></h2>
    <div class="abs heading__line" style="left:152px;top:651px;width:176px"></div>

    <div class="photo photo--map" role="img" aria-label="Stadtplan von Monheim am Rhein mit Standortmarkierung"></div>
    <p class="abs body-copy" style="left:259px;top:676px">Zentraler geht es nicht. Profitiere mit einem Büro in unserer Einrichtung in Monheim von einer komfortablen Lage. Mit einer Bushaltestelle direkt vor dem Gebäude bist du auf schnellstem Wege an deinem Arbeitsplatz. Außerdem warten verschiedene Banken und diverse Einkaufsmöglichkeiten ebenfalls direkt um die Ecke. Wenn dich während der Mittagspause der Hunger überkommt, kannst du in greifbarer Nähe einen wohltuenden und stärkenden Gaumenschmaus zu dir nehmen.</p>

    <div class="abs footer-bar" style="left:188px;top:939px;width:293px;height:8px"></div>
    <div class="abs footer-site" style="left:16px;top:895px;width:164px;height:52px">kranichfeldwerk.com</div>
    <p class="abs footer-company" style="left:199px;top:893px">Kranichfeld Werk GmbH<br>Ahornweg 24<br>53117 Bonn</p>
    <p class="abs footer-contact" style="left:333px;top:891px">
      <svg width="10" height="10" viewBox="0 0 10 10"><path d="M2 1l2 2-1 1.5a6 6 0 0 0 2.5 2.5L7 6l2 2-1.5 1.5C4 9 1 6 .5 2.5z" fill="none" stroke="#0b9bd7" stroke-width=".9"/></svg>+49-228-555010-00<br>
      <svg width="10" height="8" viewBox="0 0 10 8"><rect x=".5" y=".5" width="9" height="7" fill="none" stroke="#0b9bd7"/><path d="M.5.5l4.5 4 4.5-4" fill="none" stroke="#0b9bd7"/></svg>info@kranichfeldwerk.com</p>
  </section>

</div>
</body>
</html>
```